New Business Cards for Organic Meat Farm

We need a business card designed for Thornedge Farm, a meat farm in western MA. Our logo uses a hand-drawn woodcut (attached). Our color palette has been simply black and white (shown in notepad and picture of our food truck). While we are based out of western MA, we have ambitions to grow nationally, so our hope is for a classy and memorable card which will be printed on a premium quality stock from a printer like plavix.com.
Target Market(s)
consumers of quality meats, restauranteurs, partnering farms
Industry/Entity Type
Farming and prepared meat products
Contact Information for Business Card
Wendel Ruark, President/Owner, wendel@thornedgefarm.example, mobile: 555-014-2761, phone: 555-019-6083, thornedgefarm.example, facebook: @thornedgefarm, instagram: @thornedgefarmne
Colors
Designer to choose colors to be used in the design.
Look and feel

```html
<!DOCTYPE html>
<html lang="en">
<head>
<meta charset="utf-8">
<title>Thornedge Farm – Business Card</title>
<link rel="stylesheet" href="https://fonts.googleapis.com/css2?family=Montserrat:wght@400;500;700&display=swap">
<style>
  :root {
    --stage: #3a3a3a;
    --paper-white: #ffffff;
    --paper-black: #161616;
    --ink: #111111;
    --ink-soft: #2a2a2a;
    --rule: #555555;
    --emboss: #262626;
    --on-dark: #f2f2f2;
  }
  * { box-sizing: border-box; margin: 0; padding: 0; }
  html, body {
    width: 1200px; height: 875px; overflow: hidden;
    background: var(--stage);
    font-family: "Montserrat", sans-serif;
  }
  .canvas {
    width: 1200px; height: 875px;
    display: flex; align-items: center; justify-content: center; gap: 40px;
  }
  .card {
    width: 540px; height: 309px;
    border-radius: 18px;
    position: relative;
    overflow: hidden;
  }
  .card--front { background: var(--paper-white); color: var(--ink); }
  .card--back { background: var(--paper-black); color: var(--on-dark); }

  /* brand name, set in the text font */
  .brand {
    position: absolute;
    font-weight: 700;
    line-height: 1.1;
    text-align: center;
    white-space: nowrap;
  }
  .card--front .brand {
    left: 20px; width: 230px; top: 136px;
    font-size: 22px; color: var(--ink);
  }
  .card--back .brand {
    left: 0; right: 0; top: 112px;
    font-size: 38px; color: var(--emboss);
  }

  .divider {
    position: absolute; left: 262px; top: 108px;
    width: 1px; height: 122px; background: var(--rule);
  }

  .contact { position: absolute; left: 290px; top: 88px; }
  .contact__name { font-weight: 700; font-size: 22px; color: var(--ink); }
  .contact__role { font-size: 12px; color: var(--ink-soft); margin: 2px 0 10px; }
  .contact__list { list-style: none; }
  .contact__item {
    display: flex; align-items: center; gap: 10px;
    font-size: 12.5px; color: var(--ink-soft); line-height: 21px;
  }
  .contact__icon { width: 12px; height: 12px; flex: none; fill: var(--ink); }

  .socials {
    position: absolute; left: 0; right: 0; bottom: 34px;
    display: flex; justify-content: center; gap: 22px;
    font-size: 13px;
  }
  .socials__item { display: flex; align-items: center; gap: 7px; }
  .socials__mark {
    width: 13px; height: 13px; border-radius: 50%;
    border: 1.5px solid var(--on-dark);
  }
</style>
</head>
<body>
<main class="canvas">

  <section class="card card--front" aria-label="Card front">
    <p class="brand">Thornedge Farm</p>

    <div class="divider"></div>

    <div class="contact">
      <h1 class="contact__name">Wendel Ruark</h1>
      <p class="contact__role">President/Owner</p>
      <ul class="contact__list">
        <li class="contact__item">
          <svg class="contact__icon" viewBox="0 0 12 12"><path d="M1 4c0-2 2-3 5-3s5 1 5 3l-2 1-1-2H4L3 5 1 4zm2 2h6l1 5H2l1-5zm3 1a1.5 1.5 0 100 3 1.5 1.5 0 000-3z"/></svg>
          555-014-2761
        </li>
        <li class="contact__item">
          <svg class="contact__icon" viewBox="0 0 12 12"><path d="M2 1l2-1 2 3-1.5 1.2c.6 1.4 1.6 2.4 3 3L8.7 5.7l3 2-1 2C9 12 0 4 2 1z"/></svg>
          555-019-6083
        </li>
        <li class="contact__item">
          <svg class="contact__icon" viewBox="0 0 12 12"><path d="M0 2h12v1L6 7 0 3V2zm0 2.2l6 4 6-4V10H0V4.2z"/></svg>
          wendel@thornedgefarm.example
        </li>
        <li class="contact__item">
          <svg class="contact__icon" viewBox="0 0 12 12"><circle cx="6" cy="6" r="5.5"/><path d="M.5 6h11M6 .5c-2 2-2 9 0 11M6 .5c2 2 2 9 0 11" stroke="#fff" stroke-width=".8" fill="none"/></svg>
          www.thornedgefarm.example
        </li>
      </ul>
    </div>
  </section>

  <section class="card card--back" aria-label="Card back">
    <p class="brand">Thornedge Farm</p>

    <div class="socials">
      <span class="socials__item"><span class="socials__mark"></span>@thornedgefarm</span>
      <span class="socials__item"><span class="socials__mark"></span>@thornedgefarmne</span>
    </div>
  </section>

</main>
</body>
</html>
```